依頼概要
★作成しやすいようにラフ案をつくりましたので添付ファイルを参照よろしくお願いいたします。

急な募集で申し訳ございませんが皆さまのご参加お待ちしております。
今後も商品化が沢山ありますので良いデザイナー様には今後もお世話になりたいと思いますのでよろしくお願いいたします。
※希望は28日締め切りですが、場合によっては締め切り延長させていただきます。

■依頼の目的/概要
ヘルス&ビューティケア関連商品を集めた展示会に向け商品を買いつけするバイヤーに向けにポスターを作成お願いします。

■依頼詳細
【サイズ】 B1ポスター×2枚分

【デザイン希望】パッとみて商品の概要が分かるように素材や文字など大きめに取り、何百人も来場する方が通りすがりでも目を引くようなデザインを希望致します。

<商品概要> 10ml 無香料・無着色
※商品デザイン未定のため商品の画像入れ無でOKです

<使い方> 使い方いろいろ
化粧水・乳液・美容液・クリーム・フェイスマスク
洗顔・シャンプー・トリートメント・石鹸・ハンドクリーム
ボディケア製品など

<注目やPRポイント>
・化粧品 フェイスマスク シャンプー
・1滴混ぜるだけ!!
・美ネラルシリカ原液100% (※わざと”美ネラル”にしています)
・水晶から抽出した1滴の魔法
・いつものスキンケアがワンランクアップ

<効果と製品例のイメージデザイン>
濃厚 →原液を贅沢に
上質 →化粧水、乳液、美容液、クリーム、ハンドクリーム、フェイスマスク
濃密泡 →洗顔・シャンプー・トリートメント・石鹸
※1滴入れる事で「効果」と「製品例」を表現。アップ感のわかるイメージデザインをお願いいたします。

<画像について> 水晶から抽出した1滴イメージ画像をお願いいたします。
製品化の際にメインのデザインになりますのでよろしくお願いいたします。

その他何かご不明な点がございましたら、お気軽にご質問下さい。
よろしくお願いいたします。
依頼内容にわかりにくい表現がありましたので補足させていただきます。

B1ポスター(横728mm✕縦1030mm)を2枚並べて展示したいので、
1枚目は製品イメージとキャッチコピー
2枚目はその他製品の補足等でOKです。

カタログではなく、ポスターなので伝えたい言葉が分かりやすく、シンプルなものでokです。
■ 選んだ理由

水晶から抽出したイメージ等、美容・水晶など綺麗にまとめていただいたデザインに決めさせていただきました。

■ 提案者全員のお礼・コメント

この度は、たくさんの応募ありがとうございました。
商品ポスターではなくバイヤー向けのデザイン希望でしたので、
なかなかわかりにくい中、皆様にご応募いただいたこと感謝いたします。

```html
<!DOCTYPE html>
<html lang="ja">
<head>
<meta charset="utf-8">
<title>水晶から抽出した奇跡の一滴</title>
<link rel="stylesheet" href="https://fonts.googleapis.com/css2?family=Shippori+Mincho:wght@500&display=swap">
<style>
  :root {
    --sky-top: #e4f2fc;
    --sky-upper: #a9d4f3;
    --sky-mid: #6cb0e6;
    --sky-low: #86c0ec;
    --sky-bottom: #cfe6f7;
    --glow: rgba(255, 255, 255, 0.85);
    --crystal: #dfe8f0;
    --crystal-shade: #b9cadb;
    --ink: #ffffff;
  }
  html, body {
    margin: 0;
    padding: 0;
    width: 849px;
    height: 1200px;
    overflow: hidden;
  }
  .poster {
    position: relative;
    width: 849px;
    height: 1200px;
    overflow: hidden;
    background: linear-gradient(180deg,
      var(--sky-top) 0%,
      var(--sky-upper) 22%,
      var(--sky-mid) 55%,
      var(--sky-low) 80%,
      var(--sky-bottom) 100%);
  }
  .light-haze {
    position: absolute;
    inset: 0;
    background:
      radial-gradient(ellipse 60% 22% at 50% 8%, var(--glow), transparent 70%),
      radial-gradient(ellipse 45% 30% at 50% 100%, rgba(255,255,255,0.55), transparent 70%);
    pointer-events: none;
  }
  .crystal-cluster {
    position: absolute;
    left: 283px;
    top: 0;
    width: 311px;
    height: 140px;
    border-radius: 0 0 48% 48%;
    background: radial-gradient(ellipse at 50% 30%, #ffffff 0%, var(--crystal) 45%, var(--crystal-shade) 100%);
    opacity: 0.9;
  }
  .droplet {
    position: absolute;
    left: 383px;
    top: 335px;
    width: 84px;
    height: 120px;
  }
  .catchcopy {
    position: absolute;
    top: 655px;
    left: 486px;
    margin: 0;
    writing-mode: vertical-rl;
    font-family: "Shippori Mincho", "Noto Serif JP", serif;
    font-weight: 500;
    font-size: 64px;
    line-height: 84px;
    letter-spacing: 17px;
    color: var(--ink);
    text-shadow: 0 0 12px rgba(40, 110, 180, 0.25);
  }
  .catchcopy span { display: block; }
</style>
</head>
<body>
  <main class="poster">
    <div class="light-haze"></div>
    <div class="crystal-cluster" role="img" aria-label="水晶のクラスターから雫が落ちるイメージ"></div>

    <svg class="droplet" viewBox="0 0 84 120" aria-hidden="true">
      <defs>
        <linearGradient id="drop-fill" x1="0" y1="0" x2="0" y2="1">
          <stop offset="0" stop-color="#bfe3fb"/>
          <stop offset="0.6" stop-color="#4f9ee0"/>
          <stop offset="1" stop-color="#2f7fcb"/>
        </linearGradient>
      </defs>
      <path d="M42 2 C50 30 82 58 82 82 C82 104 64 118 42 118 C20 118 2 104 2 82 C2 58 34 30 42 2 Z"
            fill="url(#drop-fill)"/>
      <path d="M20 78 C18 92 26 104 38 108" fill="none" stroke="#ffffff" stroke-opacity="0.7" stroke-width="4" stroke-linecap="round"/>
    </svg>

    <h1 class="catchcopy">
      <span>水晶から</span>
      <span>抽出した</span>
      <span>奇跡の一滴</span>
    </h1>
  </main>
</body>
</html>
```